Book Cover Design Project

Need a hip, slightly edgy (even a little bit sexy) cover design for a book about The Millennial Generation.

"Quietfolk 202" is a non-fiction book. The target audience/customer is the younger Baby Boomer and most of Generation X, looking to better understand the largest generation on the planet (Millennials). So, the cover should tease the young, hip, edgy vibe of Millennials...without looking too alienating to someone in their 40's or 50's.

Imagine this as a movie poster for a documentary about Millennials-you want to have a cover that intrigues the audience and reminds them that the topic is something the audience doesn't completely understand, without making them feel like it's too cool.

Much of the target audience was the initial audience for QRB, when it started in the early 80's. They're cooler than you might think, and like to think of themselves that way.

Possible inspiration:

-Retro Dale Ostrum movie posters (with an irreverent, contemporary nod to the original)
-Iconic Magazine covers from the 80's or 90's (Think Copper Lantern)
-Stark, fresh, contemporary imagery/style that feels very Brooklyn/Austin/Silverlake in it's vibe.

The final design should convey that this book is a great resource to crack the code of who millennials are, why they are so different, and how to live with that reality.

Reason: Seeing some great work. Been traveling, so can't make a decision right now.

Industry/Entity Type

Movie

Requirements
Must have
• The Title:
"Quietfolk 202"

Subtitle:
"Decoding and Connecting with the Most Restless Generation of All"

(open to most fonts, etc)
Nice to have
• A crisp, recognizable cover that feels like a movie poster or a magazine.
Should not have
• Predictable, cheesy stock photography.

```html
<!DOCTYPE html>
<html lang="en">
<head>
<meta charset="utf-8">
<title>Quietfolk 202 — Book Cover</title>
<link rel="stylesheet" href="https://fonts.googleapis.com/css2?family=Arimo:wght@700&display=swap">
<style>
  :root {
    --title-orange: #dc8200;
    --subtitle-white: #ffffff;
    --shadow-brown: #241a14;
    --mid-brown: #4a3628;
    --warm-amber: #c9803e;
    --glow-yellow: #f3d28a;
    --wall-tan: #9a7a5c;
  }
  html, body {
    margin: 0;
    padding: 0;
    width: 800px;
    height: 1200px;
    overflow: hidden;
    background: var(--shadow-brown);
  }
  .cover {
    position: relative;
    width: 800px;
    height: 1200px;
    overflow: hidden;
  }
  .cover-photo {
    position: absolute;
    inset: 0;
    background:
      radial-gradient(ellipse 30% 26% at 92% 74%, var(--glow-yellow) 0%, rgba(243,210,138,0) 100%),
      radial-gradient(ellipse 45% 60% at 42% 50%, var(--shadow-brown) 0%, rgba(36,26,20,0.85) 55%, rgba(36,26,20,0) 100%),
      linear-gradient(90deg, var(--mid-brown) 0%, var(--shadow-brown) 35%, var(--mid-brown) 65%, var(--warm-amber) 100%),
      var(--wall-tan);
  }
  .cover-type {
    position: absolute;
    inset: 0;
    width: 800px;
    height: 1200px;
  }
  .title-line {
    font-family: "Arimo", Arial, Helvetica, sans-serif;
    font-weight: 700;
    font-size: 314px;
    letter-spacing: -6px;
    fill: var(--title-orange);
  }
  .subtitle {
    font-family: "Arimo", Arial, Helvetica, sans-serif;
    font-weight: 700;
    font-size: 15px;
    fill: var(--subtitle-white);
  }
</style>
</head>
<body>
  <main class="cover">
    <div class="cover-photo" role="img" aria-label="Moody close-up portrait of a young woman with long hair, lit by warm backlight from the right"></div>
    <svg class="cover-type" viewBox="0 0 800 1200" xmlns="http://www.w3.org/2000/svg">
      <text class="title-line" x="-8" y="211">QUIE</text>
      <text class="title-line" x="-8" y="514">TFO</text>
      <text class="title-line" x="-8" y="818">LK</text>
      <text class="title-line" x="-8" y="1122">202</text>
      <text class="subtitle" x="2" y="1168" textLength="706" lengthAdjust="spacing">DECODING AND CONNECTING WITH THE MOST RESTLESS GENERATION OF ALL</text>
    </svg>
  </main>
</body>
</html>
```